Flyer for teen fitness class at a physiotherapy clinic

We are a passionate Physiotherapy Clinic requiring a flyer to promote our new service a fitness class for teenagers, which is called Youth's FLX - Flexible Limber Xtra Power. The aim of the class is to prevents injuries in sports, improve sporting performance and provide safe activity for otherwise inactive teens. The aim of the flyer is to make people aware of this new service and interested in joining. Ideally the Flyer would incorporate blue colours. Our logo must be on the flier, and at least one or two of the photos provided. Our logo is provided in the attachments. Required information : Youth's FLX: Flexible Limber Xtra Power, times Mondays and Wednesdays 4 -5. Can be claimed on private health insurance. Expert advice to tailor a program to individual needs. For more information go www.rmpvq.com.au or phone 03)5871 6093.

Industry/Entity Type

Clinic

```html
<!DOCTYPE html>
<html lang="en">
<head>
<meta charset="utf-8">
<title>Youth's FLX – Riverstone Sports Treatment Clinic</title>
<link rel="stylesheet" href="https://fonts.googleapis.com/css2?family=Roboto+Condensed:wght@400;700&family=Teko:wght@500&family=Lato:wght@400;700&family=Archivo+Black&display=swap">
<style>
  :root {
    --navy: #1f3a78;
    --blue: #3b7fc8;
    --sky: #6aa6e0;
    --green: #8cc63f;
    --ink: #1d1d1f;
    --paper: #e9ebee;
    --white: #ffffff;
    --stage: #d9dbde;
  }
  * { box-sizing: border-box; margin: 0; padding: 0; }
  html, body { width: 888px; height: 1200px; overflow: hidden; background: var(--stage); }
  .flyer {
    position: absolute; left: 74px; top: 78px; width: 740px; height: 1044px;
    background: var(--paper); overflow: hidden;
    font-family: "Lato", Arial, sans-serif; color: var(--ink);
  }
  .flyer-shapes { position: absolute; inset: 0; }
  .people-photo {
    position: absolute; left: 470px; top: 655px; width: 270px; height: 389px;
    background: linear-gradient(180deg, #e4e6ea 0%, #b9bcc4 55%, #5a5e6e 100%);
  }
  .brand { position: absolute; left: 510px; top: 30px; display: flex; align-items: center; gap: 10px; }
  .brand-dot { width: 58px; height: 58px; border-radius: 50%; background: var(--blue); }
  .brand-name { font-family: "Roboto Condensed", "Arial Narrow", sans-serif; font-weight: 700; color: var(--navy); line-height: 1; }
  .brand-name .big { display: block; font-size: 30px; }
  .brand-name .small { display: block; font-size: 14px; margin-top: 3px; }
  .title { position: absolute; right: 25px; top: 138px; text-align: right; }
  .title h1 { font-family: "Roboto Condensed", "Arial Narrow", sans-serif; font-weight: 700; font-size: 52px; line-height: 1; color: var(--blue); }
  .title p { font-family: "Lato", Arial, sans-serif; font-size: 17px; margin-top: 2px; color: #222; }
  .class-heading {
    position: absolute; right: 22px; top: 378px;
    font-family: "Teko", "Arial Narrow", sans-serif; font-weight: 500; font-size: 58px; line-height: 1;
    color: var(--green); letter-spacing: 0.5px;
  }
  .benefits { position: absolute; right: 22px; top: 452px; list-style: none; text-align: right; }
  .benefits li { font-weight: 700; font-size: 19px; line-height: 26px; color: var(--blue); }
  .benefits li::after { content: "‹"; color: var(--green); font-size: 24px; margin-left: 6px; }
  .times {
    position: absolute; left: 136px; top: 598px; white-space: nowrap;
    font-family: "Teko", "Arial Narrow", sans-serif; font-weight: 500; font-size: 46px; line-height: 1; color: var(--ink);
  }
  .times .label { color: var(--blue); }
  .claim { position: absolute; left: 14px; top: 648px; width: 218px; height: 218px; }
  .claim svg { width: 218px; height: 218px; }
  .claim-text {
    position: absolute; inset: 0; display: flex; flex-direction: column; justify-content: center; align-items: center;
    font-family: "Teko", "Arial Narrow", sans-serif; font-weight: 500; font-size: 25px; line-height: 1.3; text-align: center;
  }
  .claim-text .light { color: var(--sky); }
  .claim-text .accent { color: var(--green); }
  .advice { position: absolute; left: 251px; top: 735px; width: 210px; font-size: 26px; line-height: 1.2; color: var(--ink); }
  .contact {
    position: absolute; left: 97px; top: 894px; width: 369px; height: 123px;
    background: var(--blue); border-radius: 0 12px 12px 0; padding: 10px 0 0 24px; color: var(--white);
  }
  .contact h2 { font-family: "Archivo Black", "Arial Black", sans-serif; font-weight: 400; font-size: 21px; color: var(--ink); line-height: 1.2; white-space: nowrap; }
  .contact p { font-size: 26px; line-height: 1.3; white-space: nowrap; }
</style>
</head>
<body>
<main class="flyer">
  <svg class="flyer-shapes" width="740" height="1044" viewBox="0 0 740 1044" aria-hidden="true">
    <defs>
      <linearGradient id="trainingPhotoTones" x1="0" y1="0" x2="1" y2="1">
        <stop offset="0" stop-color="#eef0f2"/>
        <stop offset="0.55" stop-color="#a9acb4"/>
        <stop offset="1" stop-color="#3e4356"/>
      </linearGradient>
    </defs>
    <path d="M0 560 Q160 590 300 520 Q420 420 470 330 Q620 300 740 380 L740 660 Q400 600 0 640 Z" fill="var(--white)"/>
    <path d="M430 222 Q600 215 740 300 L740 336 Q600 252 438 250 Z" fill="var(--navy)"/>
    <path d="M444 262 Q620 268 740 358 L740 374 Q610 292 448 282 Z" fill="var(--blue)"/>
    <path d="M85 540 Q70 600 96 660" fill="none" stroke="var(--blue)" stroke-width="10"/>
    <circle cx="205" cy="250" r="266" fill="none" stroke="var(--green)" stroke-width="4"/>
    <circle cx="205" cy="250" r="256" fill="none" stroke="var(--navy)" stroke-width="14"/>
    <circle cx="205" cy="250" r="245" fill="none" stroke="var(--blue)" stroke-width="7"/>
    <circle cx="205" cy="250" r="238" fill="url(#trainingPhotoTones)" role="img" aria-label="Photo of a teenager exercising on reformer equipment with a physiotherapist"/>
    <path d="M75 894 L97 880 L97 1017 L75 1030 Z" fill="var(--navy)"/>
  </svg>

  <div class="people-photo" role="img" aria-label="Photo of two teenagers jumping with arms raised"></div>

  <div class="brand">
    <span class="brand-dot"></span>
    <span class="brand-name"><span class="big">Riverstone</span><span class="small">Sports Treatment Clinic</span></span>
  </div>

  <header class="title">
    <h1>Youth's FLX</h1>
    <p>Flexible Limber Xtra Power</p>
  </header>

  <h2 class="class-heading">THIS CLASS</h2>
  <ul class="benefits">
    <li>Prevents injuries in sports</li>
    <li>Improve sporting performance</li>
    <li>Provides safe exercise for all fitness levels</li>
  </ul>

  <p class="times"><span class="label">TIMES</span> MONDAYS AND WEDNESDAYS 4 -5</p>

  <div class="claim">
    <svg viewBox="0 0 228 228" aria-hidden="true">
      <polygon fill="var(--navy)" points="114,2 126,28 146,7 151,35 175,20 172,48 199,41 189,68 217,68 201,91 226,101 204,117 224,136 198,143 211,168 183,168 188,195 161,187 158,215 136,199 125,226 110,203 92,224 84,198 60,212 60,184 33,190 42,164 15,160 30,137 5,125 29,111 9,91 36,83 26,57 54,58 52,30 78,40 83,12 102,30"/>
    </svg>
    <div class="claim-text">
      <span class="light">CAN BE CLAIMED ON</span>
      <span class="accent">PRIVATE HEALTH</span>
      <span class="accent">INSURANCE</span>
    </div>
  </div>

  <p class="advice">Expert advice to tailor a program to individual needs</p>

  <section class="contact">
    <h2>FOR MORE INFORMATION</h2>
    <p>www.rmpvq.com.au</p>
    <p>03)5871 6093</p>
  </section>
</main>
</body>
</html>
```